Cat sitting business Web Design Project ***

I have a cat sitting business where I either take care of cats in their home or board them in mine

I need a website which offers my services, my rates, about me, FAQ's, Hours of operation and service areas covered, testimonials, contact info, newsletter sign up, gallery of photos and the ability for me to go in and update when needed.

Coded - Design and coding required

5+ page

```html
<!DOCTYPE html>
<html lang="en">
<head>
<meta charset="utf-8">
<title>Velvet Paws Cat Care</title>
<link href="https://fonts.googleapis.com/css2?family=Poppins:wght@400;500;600;700&family=Open+Sans:wght@400;600&display=swap" rel="stylesheet">
<style>
:root{
  --rose:#b0504e;
  --rose-dark:#9c4645;
  --green:#86bf4e;
  --pink:#d9b4b6;
  --ink:#2b2b2b;
  --muted:#555;
  --night:#1d1d1d;
  --white:#fff;
}
*{box-sizing:border-box;margin:0;padding:0}
html,body{width:1200px;height:4637px;overflow:hidden}
body{font-family:"Open Sans",sans-serif;color:var(--ink);background:var(--white);position:relative}
.abs{position:absolute}
.poppins{font-family:"Poppins",sans-serif}

/* top bar */
.topbar{position:absolute;top:0;left:0;width:1200px;height:36px;background:var(--rose);color:#fff;font:400 14px "Poppins",sans-serif}
.topbar span{position:absolute;top:9px}
.topbar .sep{top:6px;width:1px;height:24px;background:rgba(255,255,255,.6)}
.dot{display:inline-block;width:9px;height:9px;border-radius:50%;background:#fff;margin-left:6px}

/* nav */
.nav{position:absolute;top:36px;left:0;width:1200px;height:84px;background:#fff;border-bottom:1px solid #eee}
.brand{position:absolute;left:92px;top:8px;width:148px;height:148px;border-radius:0 0 22px 22px;background:#fff;z-index:3;text-align:center;padding-top:50px;box-shadow:0 3px 8px rgba(0,0,0,.12)}
.brand .mark{width:40px;height:40px;border-radius:50%;background:var(--green);position:absolute;left:54px;top:8px}
.brand b{font:600 17px/1.2 "Poppins",sans-serif;color:var(--rose);display:block;margin-top:8px}
.menu{position:absolute;top:34px;left:320px;font:400 15.5px "Poppins",sans-serif;color:#333}
.menu a{position:absolute;white-space:nowrap;color:inherit;text-decoration:none}
.menu a.active{color:var(--green)}

/* hero */
.hero{position:absolute;top:120px;left:0;width:1200px;height:643px;background:radial-gradient(ellipse at 55% 60%,#9d8670 0%,#c9b8a2 40%,#e6dccd 75%,#d4c6b2 100%)}
.hero h1{position:absolute;top:92px;width:100%;text-align:center;font:600 50px "Poppins",sans-serif;color:#fff}
.hero p{position:absolute;top:164px;width:100%;text-align:center;font:400 26px "Poppins",sans-serif;color:#fff}
.btn{position:absolute;border-radius:24px;color:#fff;font:500 16px "Poppins",sans-serif;text-align:center}
.hero .btn{left:518px;top:230px;width:164px;height:44px;line-height:44px;background:var(--rose)}
.arrow{position:absolute;width:46px;height:46px;border-radius:50%;color:#fff;text-align:center;line-height:44px;font:400 20px "Poppins",sans-serif}

/* about */
.portrait{position:absolute;left:110px;top:850px;width:372px;height:385px;border-radius:50%;background:radial-gradient(circle at 45% 45%,#c9a57a,#8f6d4b 60%,#5a4431);box-shadow:-18px -12px 0 0 #c7e3b0}
.about-text{position:absolute;left:547px;top:940px;width:541px;font-size:16.5px;line-height:30px;color:#333;text-align:justify}
.about-text p{margin-bottom:8px}
.about .btn{left:547px;top:1212px;width:166px;height:44px;line-height:44px;background:var(--green);font-size:15px}

/* services */
.services{position:absolute;top:1332px;left:0;width:1200px;height:558px;background:linear-gradient(180deg,#a74c4b,#b05452);overflow:hidden}
.section-title{position:absolute;width:100%;text-align:center;font:600 50px "Poppins",sans-serif}
.rule{position:absolute;left:573px;width:54px;height:4px}
.services .section-title{top:32px;color:#fff}
.services .rule{top:110px;background:#fff}
.stage{position:absolute;left:312px;top:280px;width:576px;height:576px;border-radius:50%;background:#fff}
.stage .dash{position:absolute;inset:-22px;border:2px dashed rgba(255,255,255,.85);border-radius:50%}
.cat-photo{position:absolute;left:440px;top:325px;width:320px;height:300px;border-radius:50% 50% 0 0;background:radial-gradient(circle at 50% 45%,#9a9a98,#6f6e6b 55%,#bdbcb8)}
.svc-icon{position:absolute;width:90px;height:90px;border-radius:50%;background:#fff;box-shadow:0 2px 10px rgba(0,0,0,.2)}
.svc-icon svg{position:absolute;left:23px;top:23px;width:44px;height:44px}
.svc{position:absolute;width:240px;text-align:center;color:#fff;font-size:12.5px;line-height:20px}
.svc h3{font:600 14.5px "Poppins",sans-serif;margin-bottom:6px}

/* testimonials */
.testimonials .section-title{top:1980px;color:var(--green)}
.testimonials .rule{top:2056px;background:var(--rose)}
.card{position:absolute;top:2114px;width:455px;height:243px;background:#f6f6f6;box-shadow:0 3px 14px rgba(0,0,0,.12)}
.avatar{position:absolute;left:30px;top:32px;width:70px;height:70px;border-radius:50%;background:radial-gradient(circle,#a3805d,#e6c26b)}
.card h4{position:absolute;left:130px;top:44px;font:600 16px "Poppins",sans-serif}
.stars{position:absolute;left:130px;top:70px;color:#f1b400;font-size:12px;letter-spacing:1px}
.quote{position:absolute;right:30px;top:18px;font:700 90px/1 Georgia,serif;color:var(--rose)}
.card p{position:absolute;left:32px;top:132px;width:392px;font-size:17px;line-height:28px;text-align:justify;color:#333}

/* gallery */
.gallery{position:absolute;top:2429px;left:0;width:1200px;height:891px;background:var(--pink)}
.gallery .section-title{top:58px;color:#fff}
.gallery .rule{top:128px;background:#fff}
.tile{position:absolute}
.tile.hover{background:rgba(134,191,78,.88)}
.tile .ring{position:absolute;left:126px;top:116px;width:68px;height:68px;border:2px solid #fff;border-radius:50%}

/* faqs */
.faqs .section-title{top:3372px;color:var(--green)}
.faqs .rule{top:3448px;background:var(--rose)}
.faq{position:absolute;left:110px;width:979px;border:1px solid #ddd;background:#fff;font-size:15.5px;color:#333}
.faq .q{position:absolute;left:32px;top:31px}
.faq .toggle{position:absolute;right:12px;top:15px;width:68px;height:52px;background:var(--green);color:#fff;font:300 34px/50px "Poppins",sans-serif;text-align:center}
.faq.open{box-shadow:0 3px 12px rgba(0,0,0,.12);border:none}
.faq.open .head{position:absolute;left:0;top:0;width:100%;height:82px;background:#f4e9e9}
.faq.open .toggle{background:#fff;color:#333}
.faq.open .a{position:absolute;left:32px;top:112px}

/* footer */
.footer{position:absolute;top:4066px;left:0;width:1200px;height:571px;background:var(--night);color:#fff}
.footer .logo{position:absolute;left:110px;top:96px;font:600 30px "Poppins",sans-serif;color:var(--rose)}
.footer .logo i{position:absolute;left:12px;top:-78px;width:70px;height:70px;border-radius:50%;border:2px solid var(--green)}
.footer h5{position:absolute;font:600 16px "Poppins",sans-serif}
.signup{position:absolute;left:725px;top:108px;width:363px;height:48px;border-radius:24px;background:#fff;color:#777;font-size:15px;padding:14px 28px}
.signup i{position:absolute;right:6px;top:5px;width:38px;height:38px;border-radius:50%;background:var(--green)}
.footer .col{position:absolute;top:292px;font-size:13.5px;line-height:27px}
.footer ul{list-style:none}
.footer li::before{content:"";display:inline-block;width:6px;height:6px;border-radius:50%;background:#fff;margin:0 14px 2px 4px}
.contact-line{position:absolute;left:110px;font-size:13.5px}
.contact-line svg{position:absolute;left:0;top:-2px}
.contact-line span{padding-left:34px;display:block;line-height:29px}
.social{display:inline-block;width:32px;height:32px;border:1px solid #fff;border-radius:50%;margin-left:10px;vertical-align:middle}
.copy{position:absolute;top:516px;width:100%;text-align:center;font-size:15px}
</style>
</head>
<body>

<header class="topbar">
  <span style="left:112px">&#9742; +1 555-010-2040</span>
  <i class="sep abs" style="left:266px"></i>
  <span style="left:290px">&#9993; hello@velvetpawscatcare.com</span>
  <span style="left:752px">Create Account</span>
  <i class="sep abs" style="left:890px"></i>
  <span style="left:914px">Login</span>
  <i class="sep abs" style="left:990px"></i>
  <span style="left:1004px"><i class="dot"></i><i class="dot"></i><i class="dot"></i><i class="dot"></i></span>
</header>

<nav class="nav">
  <div class="brand"><i class="mark"></i><b>Velvet Paws<br>Cat Care</b></div>
  <div class="menu">
    <a class="active" style="left:0">Home</a>
    <a style="left:78px">Services</a>
    <a style="left:172px">My Rates</a>
    <a style="left:271px">About Me</a>
    <a style="left:375px">EAQs</a>
    <a style="left:443px">Areas Covered</a>
    <a style="left:587px">Testimonials</a>
    <a style="left:715px">Gallery</a>
  </div>
</nav>

<section class="hero" role="img" aria-label="Three kittens resting together on a soft cream blanket">
  <h1>Velvet Paws Cat Care</h1>
  <p>Cats make the rules. I just try to follow them.</p>
  <a class="btn">GET STARTED</a>
  <span class="arrow" style="left:27px;top:300px;background:rgba(90,90,90,.55)">&#8249;</span>
  <span class="arrow" style="left:1124px;top:300px;background:var(--rose)">&#8250;</span>
</section>

<section class="about">
  <div class="portrait" role="img" aria-label="Cat sitter at home holding a white cat"></div>
  <div class="about-text">
    <p>Lorem ipsum dolor sit amet, consectetur adipiscing elit, sed do eiusmod tempor incididunt ut labore et dolore magna aliqua. Ut enim ad minim veniam, quis nostrud exercitation ullamco laboris nisi ut aliquip ex ea commodo consequat. Duis aute irure dolor in reprehenderit in voluptate velit esse cillum dolore eu fugiat nulla pariatur.</p>
    <p>Lorem ipsum dolor sit amet, consectetur adipiscing elit, sed do eiusmod tempor incididunt ut labore et dolor.</p>
  </div>
  <a class="btn">LEARN MORE</a>
</section>

<section class="services">
  <h2 class="section-title">Services</h2>
  <i class="rule"></i>
  <div class="stage"><i class="dash"></i></div>
  <div class="cat-photo" role="img" aria-label="Grey tabby cat resting its paws forward"></div>

  <div class="svc" style="left:215px;top:153px"><h3>CAT WALKING</h3>Lorem ipsum dolor sit amet, consectetur adipisit, sed do eiusmod tempor incididunt ut labore et dolore</div>
  <div class="svc" style="left:724px;top:153px"><h3>HOME BOARDING</h3>Lorem ipsum dolor sit amet, consectetur adipisit, sed do eiusmod tempor incididunt ut labore et dolore</div>
  <div class="svc" style="left:108px;top:297px"><h3>CAT SITTING</h3>Lorem ipsum dolor sit amet, consectetur adipisit, sed do eiusmod tempor incididunt ut labore et dolore</div>
  <div class="svc" style="left:850px;top:297px"><h3>KITTEN CARE</h3>Lorem ipsum dolor sit amet, consectetur adipisit, sed do eiusmod tempor incididunt ut labore et dolore</div>
  <div class="svc" style="left:57px;top:439px"><h3>CAT DAY CARE</h3>Lorem ipsum dolor sit amet, consectetur adipisit, sed do eiusmod tempor incididunt ut labore et dolore</div>
  <div class="svc" style="left:921px;top:439px"><h3>CAT GROOMING</h3>Lorem ipsum dolor sit amet, consectetur adipisit, sed do eiusmod tempor incididunt ut labore et dolore</div>

  <div class="svc-icon" style="left:453px;top:228px"><svg viewBox="0 0 44 44" fill="none" stroke="#a74c4b" stroke-width="2"><ellipse cx="22" cy="30" rx="8" ry="6"/><circle cx="12" cy="18" r="4"/><circle cx="32" cy="18" r="4"/><circle cx="17" cy="10" r="3.5"/><circle cx="27" cy="10" r="3.5"/></svg></div>
  <div class="svc-icon" style="left:642px;top:228px"><svg viewBox="0 0 44 44" fill="none" stroke="#a74c4b" stroke-width="2"><path d="M5 22 22 7l17 15"/><path d="M10 18v19h24V18"/><path d="M18 37V27h8v10"/></svg></div>
  <div class="svc-icon" style="left:345px;top:301px"><svg viewBox="0 0 44 44" fill="none" stroke="#a74c4b" stroke-width="2"><rect x="8" y="14" width="28" height="22" rx="4"/><path d="M15 14v-4h14v4"/><path d="M8 24h28"/></svg></div>
  <div class="svc-icon" style="left:757px;top:301px"><svg viewBox="0 0 44 44" fill="none" stroke="#a74c4b" stroke-width="2"><path d="M22 37 7 22a8 8 0 0 1 15-10 8 8 0 0 1 15 10z"/></svg></div>
  <div class="svc-icon" style="left:291px;top:443px"><svg viewBox="0 0 44 44" fill="none" stroke="#a74c4b" stroke-width="2"><circle cx="22" cy="22" r="15"/><path d="M22 12v10l7 5"/></svg></div>
  <div class="svc-icon" style="left:829px;top:443px"><svg viewBox="0 0 44 44" fill="none" stroke="#a74c4b" stroke-width="2"><rect x="8" y="8" width="28" height="10" rx="3"/><path d="M22 18v18M16 36h12"/></svg></div>
</section>

<section class="testimonials">
  <h2 class="section-title">Testimonials</h2>
  <i class="rule"></i>
  <span class="arrow" style="left:25px;top:2225px;background:#5f5f5f">&#8249;</span>
  <span class="arrow" style="left:1122px;top:2225px;background:var(--rose)">&#8250;</span>
  <article class="card" style="left:128px">
    <i class="avatar" role="img" aria-label="Client portrait"></i>
    <h4>NORA WHITFIELD</h4><span class="stars">&#9733;&#9733;&#9733;&#9733;&#9733;</span>
    <span class="quote">&#8221;</span>
    <p>Lorem ipsum dolor sit amet, consectetur adipiscing elit, sed do eiusmod tempor incididunt ut labore et dolore magna aliqua.</p>
  </article>
  <article class="card" style="left:617px">
    <i class="avatar" role="img" aria-label="Client portrait"></i>
    <h4>NORA WHITFIELD</h4><span class="stars">&#9733;&#9733;&#9733;&#9733;&#9733;</span>
    <span class="quote">&#8221;</span>
    <p>Lorem ipsum dolor sit amet, consectetur adipiscing elit, sed do eiusmod tempor incididunt ut labore et dolore magna aliqua.</p>
  </article>
</section>

<section class="gallery">
  <h2 class="section-title">Gallery</h2>
  <i class="rule"></i>
  <div class="tile hover" style="left:112px;top:192px;width:320px;height:301px" role="img" aria-label="Woman smiling with her cat"><i class="ring"></i></div>
  <div class="tile" style="left:439px;top:192px;width:320px;height:301px;background:linear-gradient(135deg,#d9cdbd,#8a6a4c)" role="img" aria-label="Woman playing with two cats indoors"></div>
  <div class="tile" style="left:768px;top:192px;width:320px;height:301px;background:linear-gradient(135deg,#e9e4dc,#c99a6a)" role="img" aria-label="Ginger cat sleeping in a lap"></div>
  <div class="tile" style="left:112px;top:500px;width:647px;height:301px;background:linear-gradient(120deg,#e6e4df,#7c8a62 55%,#3b3b36)" role="img" aria-label="Woman hugging a cat beside house plants"></div>
  <div class="tile" style="left:768px;top:500px;width:320px;height:301px;background:radial-gradient(circle at 50% 55%,#7a6a5c,#2d2d2d)" role="img" aria-label="Three kittens sitting together"></div>
</section>

<section class="faqs">
  <h2 class="section-title">FAQs</h2>
  <i class="rule"></i>
  <div class="faq" style="top:3492px;height:85px"><span class="q">Lorem ipsum dolor sit amet, consectetur adipiscing elit, sed do eiusmod tempor incididunt?</span><span class="toggle">+</span></div>
  <div class="faq open" style="top:3592px;height:165px"><i class="head"></i><span class="q">Lorem ipsum dolor sit amet, consectetur adipiscing elit, sed do eiusmod tempor incididunt?</span><span class="toggle">&minus;</span><span class="a">Lorem ipsum dolor sit amet, consectetur adipiscing elit, sed do eiusmod tempor incididunt sed do eiusmod tempor</span></div>
  <div class="faq" style="top:3773px;height:85px"><span class="q">Lorem ipsum dolor sit amet, consectetur adipiscing elit, sed do eiusmod tempor incididunt?</span><span class="toggle">+</span></div>
  <div class="faq" style="top:3871px;height:85px"><span class="q">Lorem ipsum dolor sit amet, consectetur adipiscing elit, sed do eiusmod tempor incididunt?</span><span class="toggle">+</span></div>
</section>

<footer class="footer">
  <div class="logo"><i></i>Velvet Paws<br>Cat Care</div>
  <h5 style="left:730px;top:66px">GET OUR LATEST UPDATES</h5>
  <div class="signup">Email ID<i></i></div>

  <h5 style="left:110px;top:244px">ABOUT US</h5>
  <h5 style="left:419px;top:244px">ABOUT US</h5>
  <h5 style="left:739px;top:244px">QUICK LINKS</h5>
  <h5 style="left:943px;top:244px">OTHER LINKS</h5>

  <div class="contact-line" style="top:300px"><svg width="20" height="22" viewBox="0 0 20 22" fill="none" stroke="#fff" stroke-width="1.5"><path d="M10 21s7-7 7-12a7 7 0 0 0-14 0c0 5 7 12 7 12z"/><circle cx="10" cy="9" r="2.5"/></svg><span>Velvet Paws Cat Care,<br>Address Comes Here</span></div>
  <div class="contact-line" style="top:384px"><svg width="20" height="20" viewBox="0 0 20 20" fill="none" stroke="#fff" stroke-width="1.5"><path d="M4 2h4l2 5-3 2a11 11 0 0 0 4 4l2-3 5 2v4a2 2 0 0 1-2 2C8 18 2 12 2 4a2 2 0 0 1 2-2z"/></svg><span>ph +1 555-010-2040</span></div>
  <div class="contact-line" style="top:428px"><svg width="22" height="18" viewBox="0 0 22 18" fill="none" stroke="#fff" stroke-width="1.5"><rect x="1" y="2" width="20" height="14"/><path d="m1 2 10 8 10-8"/></svg><span>hello@velvetpawscatcare.com</span></div>

  <p class="col" style="left:419px;width:252px;text-align:justify;line-height:24px">Nemo enim ipsam voluptatem quia voluptas sit aspernatur aut odit aut fugit, sed quia emo enim ipsam voluptatem quia voluptas sit aspernatur aut odit aut fugit, sed quia.</p>
  <div class="abs" style="left:421px;top:438px;font:600 15px 'Poppins',sans-serif">FOLLOW US <i class="social"></i><i class="social"></i></div>

  <ul class="col" style="left:739px;line-height:26px">
    <li>Home</li><li>Services</li><li>My Rates</li><li>About Me</li><li>EAQs</li><li>Areas Covered</li><li>Testimonials</li><li>Gallery</li>
  </ul>
  <ul class="col" style="left:943px;line-height:26px">
    <li>Monday to Friday</li><li style="padding-left:24px">8:30 a.m - 9:00 p.m.</li><li>Saturday &amp; Sunday</li><li style="padding-left:24px">Closed</li>
  </ul>
  <p class="copy">2022 Velvet Paws Cat Care.All Rights Reserved.</p>
</footer>

</body>
</html>
```